Velto and Co Business Card Design

Looking for a business card design. Wanting Smart, Clean and Sharp looking to promote Velto and Co, our Import Export Business - like Black, White and natural textures. I have uploaded our logo. I like a rounded font but open to other ideas
Being that we have a wide range of products on offer we are looking for a neutral yet eye catching card. We would also like to have Import - Export on the business card to be clear on want our business does.

Target Market(s)

Import export market

Industry/Entity Type

Importer

Contact Information for Business Card

Mr Tobias Renwick
tobias.renwick@veltoandco.example.au
+61 (0) 412 731 846
www.veltoandco.example.au

Font styles to use
Other font styles liked:
• Unsure of actual font name but something rounded and clean

Colors

Designer to choose colors to be used in the design.

Requirements
Must have
• Pixlo icon
• Gathera icon

```html
<!DOCTYPE html>
<html lang="en">
<head>
<meta charset="utf-8">
<title>Velto and Co Business Card</title>
<link href="https://fonts.googleapis.com/css2?family=Montserrat:wght@400;600;700&display=swap" rel="stylesheet">
<style>
  :root {
    --bg: #e6e3df;
    --ink: #2b2627;
    --ink-soft: #3a3435;
    --paper: #ffffff;
    --paper-tint: #f3f2f1;
    --grey: #8d8a8a;
    --social-a: #b54a7a;
    --social-b: #3c5a99;
  }
  * { box-sizing: border-box; margin: 0; padding: 0; }
  html, body { width: 1200px; height: 900px; overflow: hidden; }
  body {
    background: var(--bg);
    font-family: "Montserrat", sans-serif;
    position: relative;
  }
  .card {
    position: absolute;
    left: 280px;
    width: 640px;
    height: 366px;
    overflow: hidden;
    box-shadow: 0 10px 28px rgba(0,0,0,.25);
  }
  .card--front { top: 56px; background: var(--ink); }
  .card--back { top: 478px; background: var(--paper-tint); }

  .brand {
    display: flex;
    align-items: center;
    gap: 14px;
    font-weight: 700;
    letter-spacing: .04em;
  }
  .brand__mark { width: 22px; height: 22px; border: 4px solid currentColor; }

  .card--front .brand {
    position: absolute; top: 86px; left: 0; right: 0;
    justify-content: center;
    color: var(--paper); font-size: 40px;
  }
  .tagline-band {
    position: absolute; top: 206px; left: 0; right: 0; height: 54px;
    background: var(--paper);
    display: flex; align-items: center; justify-content: center;
    color: var(--ink); font-weight: 600; font-size: 24px; letter-spacing: .22em;
  }
  .front-stripe {
    position: absolute; top: 292px; left: 0; right: 0; height: 16px;
    background: var(--paper);
  }

  .card--back .brand {
    position: absolute; top: 62px; left: 0; right: 0;
    justify-content: center;
    color: var(--ink); font-size: 32px;
  }
  .holder {
    position: absolute; top: 150px; left: 0; right: 0;
    text-align: center;
    color: var(--ink); font-weight: 700; font-size: 26px; letter-spacing: .08em;
  }
  .social {
    position: absolute; top: 0; right: 0; height: 48px; width: 230px;
    background: var(--ink);
    clip-path: polygon(12% 0, 100% 0, 100% 100%, 0 100%);
    display: flex; align-items: center; justify-content: flex-end;
    gap: 14px; padding-right: 18px;
    color: var(--paper); font-size: 13px; font-weight: 600;
  }
  .social__item { display: flex; align-items: center; gap: 6px; }
  .social__dot { width: 18px; height: 18px; border-radius: 50%; }
  .social__dot--a { background: var(--social-a); }
  .social__dot--b { background: var(--social-b); }

  .contact {
    position: absolute; left: 0; right: 0; bottom: 0; height: 128px;
    background: var(--ink);
    padding: 16px 0 0 36px;
    list-style: none;
    color: var(--paper); font-size: 19px;
  }
  .contact li { display: flex; align-items: center; gap: 12px; height: 33px; }
  .contact svg { width: 20px; height: 20px; flex: none; }
</style>
</head>
<body>
  <section class="card card--front">
    <div class="brand"><span class="brand__mark"></span>Velto and Co</div>
    <div class="tagline-band">Import &amp; Export</div>
    <div class="front-stripe"></div>
  </section>

  <section class="card card--back">
    <div class="social">
      <span class="social__item"><span class="social__dot social__dot--a"></span>Pixlo</span>
      <span class="social__item"><span class="social__dot social__dot--b"></span>Gathera</span>
    </div>
    <div class="brand"><span class="brand__mark"></span>Velto and Co</div>
    <p class="holder">Mr. Tobias Renwick</p>
    <ul class="contact">
      <li>
        <svg viewBox="0 0 20 20"><circle cx="10" cy="10" r="10" fill="#8d8a8a"/><rect x="5" y="6.5" width="10" height="7" fill="none" stroke="#2b2627" stroke-width="1.4"/><path d="M5 6.5l5 4 5-4" fill="none" stroke="#2b2627" stroke-width="1.4"/></svg>
        tobias.renwick@veltoandco.example.au
      </li>
      <li>
        <svg viewBox="0 0 20 20"><circle cx="10" cy="10" r="10" fill="#8d8a8a"/><path d="M7 5.5l2 2.5-1 1.2a6 6 0 0 0 2.8 2.8l1.2-1 2.5 2-1.2 1.6C9.5 14.5 5.5 10.5 5.4 6.7z" fill="#2b2627"/></svg>
        +61 (0) 412 731 846
      </li>
      <li>
        <svg viewBox="0 0 20 20"><circle cx="10" cy="10" r="10" fill="#8d8a8a"/><circle cx="10" cy="10" r="5" fill="none" stroke="#2b2627" stroke-width="1.3"/><path d="M5 10h10M10 5c-2.5 3-2.5 7 0 10M10 5c2.5 3 2.5 7 0 10" fill="none" stroke="#2b2627" stroke-width="1.1"/></svg>
        www.veltoandco.example.au
      </li>
    </ul>
  </section>
</body>
</html>
```